Verdanix Medical Business Card

Create a high class Business card for Medical Aesthetics and Wellness Practice called Verdanix Medical Aesthetics and Wellness as per the logo attached.
Addresss is: 418 Harlan Brook Road Suite 312 Melville, New York 11093
Phone (555)204-7391 IG @verdanix_medical
Verdanixmedical.example

I need 5 different name configurations
1) Dr. Theo Valcourt
Aesthetics and Wellness Specialist
Medical Director

2) Rosalind Pettinger, NP
Clinical Nurse Manager

3) Marla Vostrik, RN
Aesthetic Nurse Specialist

4) Petra Halvesen, RN

5) Dana Kowbeck, L.E.
Senior Licensed Esthetician

Target Market(s)

22-55 Females

Industry/Entity Type

Medical Spa and Wellness

Contact Information for Business Card

Logo, address, phone, web, instagram, providers name

Requirements
Must have
• Attractive classy modern look

```html
<!DOCTYPE html>
<html lang="en">
<head>
<meta charset="utf-8">
<title>Verdanix Medical Business Card</title>
<link rel="stylesheet" href="https://fonts.googleapis.com/css2?family=Cormorant+Garamond:wght@400;500&family=Poppins:ital,wght@0,500;0,700;1,500&display=swap">
<style>
  :root {
    --backdrop: #73c3c7;
    --navy: #0f4e61;
    --navy-soft: #19596b;
    --ink: #0d4b5e;
    --icon: #5fb3b9;
    --paper: #ffffff;
  }
  * { margin: 0; padding: 0; box-sizing: border-box; }
  html, body { width: 1200px; height: 1200px; overflow: hidden; }
  body {
    position: relative;
    background: var(--backdrop);
    font-family: "Poppins", sans-serif;
  }
  .card {
    position: absolute;
    left: 183px;
    width: 834px;
    height: 476px;
  }
  .card-front { top: 119px; }
  .card-back { top: 606px; background: var(--paper); }

  .front-texture {
    position: absolute;
    inset: 0;
    background: linear-gradient(160deg, var(--navy) 0%, var(--navy-soft) 50%, var(--navy) 100%);
  }

  .brand {
    position: absolute;
    left: 0;
    right: 0;
    text-align: center;
    font-family: "Cormorant Garamond", serif;
    font-weight: 400;
    line-height: 1;
  }
  .brand-name { letter-spacing: 0.14em; }
  .brand-tagline { letter-spacing: 0.04em; text-transform: uppercase; }
  .brand-place { letter-spacing: 0.55em; text-transform: uppercase; }

  .card-front .brand { color: var(--paper); }
  .card-front .brand-name { top: 170px; font-size: 66px; }
  .card-front .brand-tagline { top: 250px; font-size: 20px; }
  .card-front .brand-place { top: 285px; font-size: 13px; }

  .back-logo {
    position: absolute;
    left: 98px;
    width: 190px;
    top: 0;
    height: 476px;
  }
  .back-logo .brand { color: var(--ink); left: -20px; right: -20px; }
  .back-logo .brand-name { top: 198px; font-size: 29px; }
  .back-logo .brand-tagline { top: 243px; font-size: 10px; }
  .back-logo .brand-place { top: 258px; font-size: 7px; }

  .person {
    position: absolute;
    left: 483px;
    top: 122px;
    color: var(--ink);
  }
  .person-name {
    font-weight: 700;
    font-size: 25px;
    letter-spacing: -0.045em;
    line-height: 1;
    text-transform: uppercase;
  }
  .person-role {
    margin-top: 6px;
    font-style: italic;
    font-weight: 500;
    font-size: 16px;
    line-height: 1.1;
  }
  .contact-list {
    list-style: none;
    margin-top: 32px;
  }
  .contact-item {
    display: flex;
    align-items: center;
    height: 31px;
    font-weight: 500;
    font-size: 17px;
  }
  .contact-icon {
    width: 16px;
    height: 16px;
    margin-right: 20px;
    flex: none;
  }
  .contact-icon svg { display: block; }
  .address {
    margin-top: 26px;
    font-style: normal;
    font-weight: 500;
    font-size: 17px;
    line-height: 20px;
  }
</style>
</head>
<body>
  <section class="card card-front">
    <div class="front-texture" role="img" aria-label="Subtle tonal pattern across the card front"></div>
    <div class="brand brand-name">Verdanix</div>
    <div class="brand brand-tagline">Medical Aesthetics and Wellness</div>
    <div class="brand brand-place">New York</div>
  </section>

  <section class="card card-back">
    <div class="back-logo">
      <div class="brand brand-name">Verdanix</div>
      <div class="brand brand-tagline">Medical Aesthetics and Wellness</div>
      <div class="brand brand-place">New York</div>
    </div>

    <div class="person">
      <h1 class="person-name">Dr. Theo Valcourt</h1>
      <p class="person-role">Medical Director</p>
      <ul class="contact-list">
        <li class="contact-item">
          <span class="contact-icon">
            <svg width="16" height="16" viewBox="0 0 16 16" fill="none" stroke="var(--icon)" stroke-width="1.2">
              <circle cx="8" cy="8" r="7"/>
              <ellipse cx="8" cy="8" rx="3" ry="7"/>
              <line x1="1" y1="8" x2="15" y2="8"/>
              <path d="M2.2 4.5h11.6M2.2 11.5h11.6"/>
            </svg>
          </span>
          verdanixmedical.example
        </li>
        <li class="contact-item">
          <span class="contact-icon">
            <svg width="16" height="16" viewBox="0 0 16 16" fill="none" stroke="var(--icon)" stroke-width="1.2" stroke-linejoin="round">
              <path d="M3.5 1.5l2.5 0.3 1 3-1.6 1.3c0.9 1.9 2.2 3.2 4.1 4.1l1.3-1.6 3 1 0.3 2.5c-0.3 1-1.2 1.6-2.2 1.6C6.5 13.5 2.5 9.5 2 4c0-1.1 0.6-2 1.5-2.5z"/>
            </svg>
          </span>
          (555)204-7391
        </li>
        <li class="contact-item">
          <span class="contact-icon">
            <svg width="16" height="16" viewBox="0 0 16 16" fill="none" stroke="var(--icon)" stroke-width="1.2">
              <rect x="1.5" y="1.5" width="13" height="13" rx="3"/>
            </svg>
          </span>
          @verdanix_medical
        </li>
      </ul>
      <address class="address">
        418 Harlan Brook Road Suite 312<br>
        Melville, New York 11093
      </address>
    </div>
  </section>
</body>
</html>
```